Kestrel Aid Services Banner Ad

Need a 750 x 250-pixel banner ad with the company Logo included. Please see company website at www.kestrelaidservices.com for more information.

```html
<!DOCTYPE html>
<html lang="en">
<head>
<meta charset="utf-8">
<title>Kestrel Aid Services Banner</title>
<link rel="stylesheet" href="https://fonts.googleapis.com/css2?family=Poppins:wght@400;700;800&display=swap">
<style>
  :root {
    --page-bg: #e4e4e4;
    --navy: #031f42;
    --green: #6cc51f;
    --white: #ffffff;
    --photo-light: #8fbf5a;
    --photo-dark: #4f7f2c;
  }
  * { margin: 0; padding: 0; box-sizing: border-box; }
  html, body {
    width: 1200px; height: 1200px; overflow: hidden;
    background: var(--page-bg);
    font-family: "Poppins", sans-serif;
  }
  .banner {
    position: absolute; left: 30px; top: 410px;
    width: 1140px; height: 380px;
    background: var(--white);
    overflow: hidden;
  }
  .banner-shapes { position: absolute; inset: 0; }
  .brand {
    position: absolute; right: 50px; top: 52px;
    display: flex; align-items: center; gap: 14px;
  }
  .brand-dot {
    width: 30px; height: 30px; border-radius: 50%;
    background: var(--navy);
  }
  .brand-name {
    font-weight: 700; font-size: 36px; line-height: 1;
    color: var(--green);
  }
  .headline {
    position: absolute; right: 50px; top: 186px;
    text-align: right; font-weight: 800; text-transform: uppercase;
    line-height: 1.15;
  }
  .headline-top { color: var(--green); font-size: 38px; letter-spacing: 0.2px; }
  .headline-bottom { color: var(--white); font-size: 45px; }
  .cta {
    position: absolute; left: 842px; top: 296px;
    width: 248px; height: 41px;
    border: 1.5px solid var(--white); border-radius: 21px;
    display: flex; align-items: center; justify-content: center; gap: 10px;
    color: var(--green); font-size: 21px; font-weight: 400;
    text-transform: uppercase;
  }
  .cta-icon { width: 20px; height: 20px; }
</style>
</head>
<body>
  <div class="banner">
    <svg class="banner-shapes" width="1140" height="380" viewBox="0 0 1140 380">
      <defs>
        <linearGradient id="photoTone" x1="0" y1="0" x2="1" y2="1">
          <stop offset="0" stop-color="var(--photo-light)"/>
          <stop offset="0.6" stop-color="var(--photo-dark)"/>
          <stop offset="1" stop-color="#9cc4d8"/>
        </linearGradient>
      </defs>
      <polygon points="0,0 694,0 412,380 0,380" fill="url(#photoTone)" role="img"
        aria-label="Photo of a woman blowing dandelion seeds on a green lawn"/>
      <path d="M612,143 L1140,143 L1140,380 L426,380 L592,154 Q600,143 612,143 Z" fill="var(--navy)"/>
    </svg>

    <div class="brand">
      <span class="brand-dot"></span>
      <span class="brand-name">Kestrel Aid Services</span>
    </div>

    <div class="headline">
      <div class="headline-top">Support Coordination</div>
      <div class="headline-bottom">Across New Jersey</div>
    </div>

    <div class="cta">
      <span>Learn More</span>
      <svg class="cta-icon" viewBox="0 0 20 20">
        <circle cx="10" cy="10" r="10" fill="var(--green)"/>
        <polyline points="8,5.5 12.5,10 8,14.5" fill="none" stroke="var(--white)" stroke-width="2.4" stroke-linecap="round" stroke-linejoin="round"/>
      </svg>
    </div>
  </div>
</body>
</html>
```